Design refresh / update on current website (design only)

I currently have this website - www.pulse-harbor.net and I would like a refresh / update on it
Primarily, I would like the events page re designed as that is the most important page -
www.pulse-harbor.net/events
I would like it done to look like this in terms of layout -
https://www.thebrixdepot.net/club-events/
(But without looking like it is a direct copy)
But I do not like the more pastel type look of this example website, instead I would like a sharper more digital look and feel like it is at the moment or like -
https://vornitude.net/events
www.zqtmornings.net
https://www.palaceofechoes.net/club/
It MUST have that sharp digital look and feel
And to look at the top bit of the website with the following menu options -
HOME
EVENTS
SHOP
HIRE
EXPERIENCES
ARTIST BOOKINGS
CONTACT
I am thinking once this is nailed, the home page and rest of the site can then be worked on as a separate project
There is also a ''bassline beats for a bassline crowd'' slogan which I would like added somewhere or it can be saved for just the home page or the bottom of pages
I would also like a filter button on the events so you can filter by -
All Events
Festivals
Brunches
Clubs
Amsterdam
Abroad
Experiences
UK Tour
It must at the very least look of equal standard as the brix depot look and feel
Go with the rectangle buttons rather than the current ones and move away from the pink current colours to look a bit cooler
Number of Pages Required
1 page
Look and feel

```html
<!DOCTYPE html>
<html lang="en">
<head>
<meta charset="utf-8">
<title>Pulse Harbor Events</title>
<link rel="stylesheet" href="https://fonts.googleapis.com/css2?family=Oswald:wght@400;500;600&family=Roboto:wght@400;500&display=swap">
<style>
:root{
  --page:#191919;
  --card:#1b1b1b;
  --card-line:#2c2c2c;
  --title:#bcbcbc;
  --muted:#8a8a8a;
  --date:#8f8f8f;
  --accent:#8b3ff2;
  --white:#ffffff;
  --band:#4b2a80;
  --footer:#161616;
  --btn-line:#4a4a4a;
}
*{box-sizing:border-box;margin:0;padding:0}
html,body{width:1200px;height:3409px;overflow:hidden}
body{background:var(--page);font-family:Roboto,Arial,sans-serif;color:var(--white);position:relative}
.hero{position:relative;height:611px;background:radial-gradient(ellipse at 50% 10%,#8a4a3a 0%,#5a3128 35%,#2a1a16 70%,#181210 100%)}
.hero-photo{position:absolute;inset:0}
.topbar{position:absolute;top:0;left:0;right:0;height:100px;display:flex;align-items:center}
.brand{position:absolute;left:103px;top:30px;font-family:Oswald,sans-serif;font-weight:600;font-size:32px;letter-spacing:1px;color:#d9d9d9;text-transform:uppercase}
.nav{position:absolute;left:490px;top:40px;display:flex;gap:0;font-family:Oswald,sans-serif;font-size:14px;font-weight:500;text-transform:uppercase}
.nav a{color:var(--white);text-decoration:none;margin-right:36px;position:relative}
.nav a.current::after{content:"";position:absolute;left:0;right:0;bottom:-8px;height:2px;background:var(--white)}
.hero-name{position:absolute;top:250px;left:0;right:0;text-align:center;font-family:Oswald,sans-serif;font-weight:600;font-size:60px;letter-spacing:3px;text-transform:uppercase}
.hero-slogan{position:absolute;top:362px;left:0;right:0;text-align:center;font-family:Roboto,Arial,sans-serif;font-size:45px;font-weight:400}
.events{padding-top:678px;position:absolute;top:0;left:0;right:0}
.events-title{text-align:center;font-family:Oswald,sans-serif;font-weight:500;font-size:60px;letter-spacing:1px;line-height:72px;text-transform:uppercase}
.filters{display:flex;justify-content:center;gap:39px;margin-top:22px;font-size:15.5px;color:#bdbdbd}
.filters span.active{color:var(--white);border-bottom:2px solid var(--white);padding-bottom:4px}
.event-list{position:absolute;top:844px;left:147px;width:901px}
.event{position:relative;height:180px;margin-bottom:15px;background:var(--card);border:1px solid var(--card-line)}
.event-photo{position:absolute;left:0;top:0;width:196px;height:179px}
.event-notch{position:absolute;left:196px;top:0;width:41px;height:20px}
.event-date{position:absolute;left:196px;top:60px;width:92px;text-align:center;font-family:Oswald,sans-serif;color:var(--date);text-transform:uppercase}
.event-date .month{display:block;font-size:19px;line-height:20px;font-weight:500}
.event-date .day{display:block;font-size:46px;line-height:50px;font-weight:500}
.event-info{position:absolute;left:305px;top:54px}
.event-name{font-family:Oswald,sans-serif;font-weight:500;font-size:23px;color:var(--title);text-transform:uppercase;line-height:30px}
.event-venue,.event-when{display:flex;align-items:center;gap:9px;font-size:12.5px;margin-top:5px}
.event-venue{color:var(--accent);text-transform:uppercase;margin-top:8px}
.event-when{color:var(--muted)}
.event-btn{position:absolute;left:696px;top:60px;width:171px;height:51px;border:2px solid var(--btn-line);display:flex;align-items:center;justify-content:center;font-family:Oswald,sans-serif;font-weight:500;font-size:15px;color:#8c8c8c;letter-spacing:.5px}
.signup{position:absolute;top:2666px;left:0;right:0;height:333px;background:linear-gradient(180deg,#4e2b86,#46287a);text-align:center}
.signup-title{margin-top:84px;font-family:Oswald,sans-serif;font-weight:600;font-size:44px;text-transform:uppercase;line-height:52px}
.signup-text{margin-top:12px;font-size:17px}
.signup-form{display:flex;justify-content:center;gap:9px;margin-top:22px}
.signup-input{width:354px;height:48px;border-radius:24px;background:var(--white);color:#555;font-size:16px;text-align:left;padding:14px 24px}
.signup-btn{width:160px;height:48px;border-radius:24px;background:#0d0d0d;font-family:Oswald,sans-serif;font-weight:600;font-size:22px;line-height:48px;text-transform:uppercase}
.footer{position:absolute;top:2999px;left:0;right:0;height:410px;background:var(--footer)}
.footer-brand{position:absolute;left:153px;top:118px;font-family:Oswald,sans-serif;font-weight:600;font-size:38px;line-height:36px;color:#cfcfcf;text-transform:uppercase}
.copyright{position:absolute;left:157px;top:270px;font-size:14px}
.footer-rule{position:absolute;left:447px;top:77px;width:1px;height:251px;background:#3a3a3a}
.footer-col{position:absolute;top:104px}
.footer-col h4{font-family:Oswald,sans-serif;font-weight:500;font-size:18px;text-transform:uppercase;margin-bottom:14px}
.footer-col a{display:block;color:#9a9a9a;font-size:12px;text-decoration:none;margin-bottom:10px;text-transform:none}
.footer-col.upper a{text-transform:uppercase}
.contact-mail{text-decoration:underline!important}
.follow{margin-top:34px}
.socials{display:flex;gap:7px}
.socials span{width:30px;height:30px;border:1.5px solid var(--white);border-radius:50%}
</style>
</head>
<body>
<header class="hero">
  <div class="hero-photo" role="img" aria-label="Crowd with raised hands in a dimly lit concert venue"></div>
  <div class="brand">Pulse Harbor</div>
  <nav class="nav">
    <a href="#">Home</a><a href="#" class="current">Events</a><a href="#">Shop</a><a href="#">Hire</a><a href="#">Experiences</a><a href="#">Artist Bookings</a><a href="#">Contact</a>
  </nav>
  <div class="hero-name">Pulse Harbor</div>
  <p class="hero-slogan">bassline beats for a bassline crowd</p>
</header>

<section class="events">
  <h1 class="events-title">Pulse Harbor Events</h1>
  <div class="filters">
    <span class="active">All Events</span><span>Festivals</span><span>Brunches</span><span>Clubs</span><span>Amsterdam</span><span>Abroad</span><span>Experiences</span><span>UK Tour</span>
  </div>
</section>

<div class="event-list">
  <article class="event">
    <div class="event-photo" role="img" aria-label="Dancers under purple and red club lights" style="background:linear-gradient(135deg,#6a1a4a,#3a2070,#18102a)"></div>
    <div class="event-notch" style="background:#5a2a70"></div>
    <div class="event-date"><span class="month">Nov</span><span class="day">26</span></div>
    <div class="event-info">
      <h2 class="event-name">Pulse Harbor Milton Keynes</h2>
      <p class="event-venue"><svg width="8" height="11" viewBox="0 0 8 11"><path d="M4 0a4 4 0 0 1 4 4c0 3-4 7-4 7S0 7 0 4a4 4 0 0 1 4-4z" fill="#8b3ff2"/><circle cx="4" cy="4" r="1.5" fill="#1b1b1b"/></svg>Unit Eleven</p>
      <p class="event-when"><svg width="9" height="9" viewBox="0 0 9 9"><rect x="0" y="1" width="9" height="8" fill="#6a6a6a"/></svg>Saturday 26th november 2022</p>
    </div>
    <div class="event-btn">BUY TICKETS</div>
  </article>
  <article class="event">
    <div class="event-photo" role="img" aria-label="Large crowd facing a lit stage" style="background:linear-gradient(160deg,#2a2a50,#5a3050,#1a1a30)"></div>
    <div class="event-notch" style="background:#6a4a5a"></div>
    <div class="event-date"><span class="month">Nov</span><span class="day">26</span></div>
    <div class="event-info">
      <h2 class="event-name">Pulse Harbor Biggleswade</h2>
      <p class="event-venue"><svg width="8" height="11" viewBox="0 0 8 11"><path d="M4 0a4 4 0 0 1 4 4c0 3-4 7-4 7S0 7 0 4a4 4 0 0 1 4-4z" fill="#8b3ff2"/><circle cx="4" cy="4" r="1.5" fill="#1b1b1b"/></svg>Biggleswade</p>
      <p class="event-when"><svg width="9" height="9" viewBox="0 0 9 9"><rect x="0" y="1" width="9" height="8" fill="#6a6a6a"/></svg>Saturday 26th november 2022</p>
    </div>
    <div class="event-btn">BUY TICKETS</div>
  </article>
  <article class="event">
    <div class="event-photo" role="img" aria-label="Friends celebrating at a brunch party" style="background:linear-gradient(135deg,#2a8a90,#7a5a30,#3a2a1a)"></div>
    <div class="event-notch" style="background:#2aa0b0"></div>
    <div class="event-date"><span class="month">Dec</span><span class="day">03</span></div>
    <div class="event-info">
      <h2 class="event-name">Pulse Harbor Christmas Brunch</h2>
      <p class="event-venue"><svg width="8" height="11" viewBox="0 0 8 11"><path d="M4 0a4 4 0 0 1 4 4c0 3-4 7-4 7S0 7 0 4a4 4 0 0 1 4-4z" fill="#8b3ff2"/><circle cx="4" cy="4" r="1.5" fill="#1b1b1b"/></svg>Vela, Kings Cross</p>
      <p class="event-when"><svg width="9" height="9" viewBox="0 0 9 9"><rect x="0" y="1" width="9" height="8" fill="#6a6a6a"/></svg>Saturday 3rd December&nbsp; 2022</p>
    </div>
    <div class="event-btn">BUY TICKETS</div>
  </article>
  <article class="event">
    <div class="event-photo" role="img" aria-label="Crowd silhouettes under blue stage lights" style="background:linear-gradient(160deg,#1a8ad0,#0a3a80,#061428)"></div>
    <div class="event-notch" style="background:#e8e8f0"></div>
    <div class="event-date"><span class="month">Dec</span><span class="day">10</span></div>
    <div class="event-info">
      <h2 class="event-name">Bassline Bingo &amp; Brunch</h2>
      <p class="event-venue"><svg width="8" height="11" viewBox="0 0 8 11"><path d="M4 0a4 4 0 0 1 4 4c0 3-4 7-4 7S0 7 0 4a4 4 0 0 1 4-4z" fill="#8b3ff2"/><circle cx="4" cy="4" r="1.5" fill="#1b1b1b"/></svg>Reelbox Romford</p>
      <p class="event-when"><svg width="9" height="9" viewBox="0 0 9 9"><rect x="0" y="1" width="9" height="8" fill="#6a6a6a"/></svg>Saturday 10th December&nbsp; 2022</p>
    </div>
    <div class="event-btn">BUY TICKETS</div>
  </article>
  <article class="event">
    <div class="event-photo" role="img" aria-label="DJ decks with dancers under red and blue lights" style="background:linear-gradient(135deg,#c02a40,#3a2a80,#101020)"></div>
    <div class="event-notch" style="background:#4a2aa0"></div>
    <div class="event-date"><span class="month">Dec</span><span class="day">10</span></div>
    <div class="event-info">
      <h2 class="event-name">Pulse Harbor Maidstone</h2>
      <p class="event-venue"><svg width="8" height="11" viewBox="0 0 8 11"><path d="M4 0a4 4 0 0 1 4 4c0 3-4 7-4 7S0 7 0 4a4 4 0 0 1 4-4z" fill="#8b3ff2"/><circle cx="4" cy="4" r="1.5" fill="#1b1b1b"/></svg>Maidstone</p>
      <p class="event-when"><svg width="9" height="9" viewBox="0 0 9 9"><rect x="0" y="1" width="9" height="8" fill="#6a6a6a"/></svg>Saturday 10th December&nbsp; 2022</p>
    </div>
    <div class="event-btn">BUY TICKETS</div>
  </article>
  <article class="event">
    <div class="event-photo" role="img" aria-label="Festive party crowd in holiday hats" style="background:linear-gradient(135deg,#8a8a8a,#5a4a40,#2a2420)"></div>
    <div class="event-notch" style="background:#b0b0b0"></div>
    <div class="event-date"><span class="month">Dec</span><span class="day">23</span></div>
    <div class="event-info">
      <h2 class="event-name">Pulse Harbor 25th Year Birthday</h2>
      <p class="event-venue"><svg width="8" height="11" viewBox="0 0 8 11"><path d="M4 0a4 4 0 0 1 4 4c0 3-4 7-4 7S0 7 0 4a4 4 0 0 1 4-4z" fill="#8b3ff2"/><circle cx="4" cy="4" r="1.5" fill="#1b1b1b"/></svg>Maidstone</p>
      <p class="event-when"><svg width="9" height="9" viewBox="0 0 9 9"><rect x="0" y="1" width="9" height="8" fill="#6a6a6a"/></svg>Saturday 23rd December 2022</p>
    </div>
    <div class="event-btn">BUY TICKETS</div>
  </article>
  <article class="event">
    <div class="event-photo" role="img" aria-label="Confetti falling over a dancing crowd in pink light" style="background:linear-gradient(135deg,#a02040,#5a1a3a,#200a18)"></div>
    <div class="event-notch" style="background:#c03050"></div>
    <div class="event-date"><span class="month">Feb</span><span class="day">10</span></div>
    <div class="event-info">
      <h2 class="event-name">Pulse Harbor St Ives UK Tour</h2>
      <p class="event-venue"><svg width="8" height="11" viewBox="0 0 8 11"><path d="M4 0a4 4 0 0 1 4 4c0 3-4 7-4 7S0 7 0 4a4 4 0 0 1 4-4z" fill="#8b3ff2"/><circle cx="4" cy="4" r="1.5" fill="#1b1b1b"/></svg>St Ives</p>
      <p class="event-when"><svg width="9" height="9" viewBox="0 0 9 9"><rect x="0" y="1" width="9" height="8" fill="#6a6a6a"/></svg>Friday 10th February 2023</p>
    </div>
    <div class="event-btn">BUY TICKETS</div>
  </article>
  <article class="event">
    <div class="event-photo" role="img" aria-label="Crowd silhouettes against warm golden lights" style="background:radial-gradient(circle at 40% 30%,#f0a030,#b04a20 45%,#2a0e08)"></div>
    <div class="event-notch" style="background:#d06020"></div>
    <div class="event-date"><span class="month">Mar</span><span class="day">11</span></div>
    <div class="event-info">
      <h2 class="event-name">Pulse Harbor Southampton</h2>
      <p class="event-venue"><svg width="8" height="11" viewBox="0 0 8 11"><path d="M4 0a4 4 0 0 1 4 4c0 3-4 7-4 7S0 7 0 4a4 4 0 0 1 4-4z" fill="#8b3ff2"/><circle cx="4" cy="4" r="1.5" fill="#1b1b1b"/></svg>Southampton</p>
      <p class="event-when"><svg width="9" height="9" viewBox="0 0 9 9"><rect x="0" y="1" width="9" height="8" fill="#6a6a6a"/></svg>Saturday 11th March 2023</p>
    </div>
    <div class="event-btn">BUY TICKETS</div>
  </article>
  <article class="event">
    <div class="event-photo" role="img" aria-label="Confetti over a crowd under blue and red lights" style="background:linear-gradient(135deg,#2050c0,#6a2a80,#a02040)"></div>
    <div class="event-notch" style="background:#b02040"></div>
    <div class="event-date"><span class="month">Mar</span><span class="day">18</span></div>
    <div class="event-info">
      <h2 class="event-name">Pulse Harbor Brighton</h2>
      <p class="event-venue"><svg width="8" height="11" viewBox="0 0 8 11"><path d="M4 0a4 4 0 0 1 4 4c0 3-4 7-4 7S0 7 0 4a4 4 0 0 1 4-4z" fill="#8b3ff2"/><circle cx="4" cy="4" r="1.5" fill="#1b1b1b"/></svg>Brighton</p>
      <p class="event-when"><svg width="9" height="9" viewBox="0 0 9 9"><rect x="0" y="1" width="9" height="8" fill="#6a6a6a"/></svg>Saturday 18th March 2023</p>
    </div>
    <div class="event-btn">BUY TICKETS</div>
  </article>
</div>

<section class="signup">
  <h2 class="signup-title">Keep Up To Date</h2>
  <p class="signup-text">Sign Up to receive exclusive discounts &amp; pre sale links before anyone else!</p>
  <div class="signup-form">
    <div class="signup-input">Email:</div>
    <div class="signup-btn">Subscribe</div>
  </div>
</section>

<footer class="footer">
  <div class="footer-brand">Pulse<br>Harbor<br>Brunch</div>
  <p class="copyright">© Pulse Harbor 2022</p>
  <div class="footer-rule"></div>
  <div class="footer-col" style="left:565px">
    <h4>Contact Us</h4>
    <a href="#" class="contact-mail">support@pulse-harbor.net</a>
    <h4 class="follow">Follow Us</h4>
    <div class="socials"><span></span><span></span><span></span><span></span></div>
  </div>
  <div class="footer-col upper" style="left:822px">
    <h4>Links</h4>
    <a href="#">Home</a><a href="#">Events</a><a href="#">Shop</a><a href="#">Hire</a><a href="#">Experiences</a><a href="#">Artist Bookings</a><a href="#">Contact</a>
  </div>
  <div class="footer-col" style="left:978px">
    <h4>Events</h4>
    <a href="#">Festivals</a><a href="#">Brunches</a><a href="#">Clubs</a><a href="#">Amsterdam</a><a href="#">Abroad</a><a href="#">Experiences</a><a href="#">UK Tour</a>
  </div>
</footer>
</body>
</html>
```